Tour agency for FIT and groups need a business card design

We need a business card design for a tour agency company that is based in Perth called" BRISK NO", we aim to provide customise, unique and seamless travel arrangement for FIT and groups. We serve both high profile businessperson, government authorities, business partners, executives and investors. The name card should be more professional looking.
Updates

Project Deadline Extended Reason: Have some changes that needed to make, director will be back to office on Monday, sorry for the inconvenience cause. Added Saturday, May 6, 2017

Target Market(s)

High profile businessperson, government authorities, business partners, executives and investors.

Industry/Entity Type

Tourism

Contact Information for Business Card

Brisk NO
Level 1, 214 Marlowe Avenue, Dunreath NO, 6120
www.briskno.com.au

Font styles to use
Serif

Colors

Designer to choose colors to be used in the design.

Requirements
Must have
• My project must have a company logo
Nice to have
• a more professional and solid yet friendly name card design. We may want to include chinese name in the name card as well. Edge of the card can be filled with gold and we think that transparent name cards are interesting.

```html
<!DOCTYPE html>
<html lang="en">
<head>
<meta charset="utf-8">
<title>Brisk NO – Business Card</title>
<link href="https://fonts.googleapis.com/css2?family=Fira+Sans+Condensed:wght@400;500;800&display=swap" rel="stylesheet">
<style>
  :root {
    --bg: #ebe9e5;
    --card-black: #1a1718;
    --card-white: #f7f6f3;
    --gold: #d2a056;
    --accent: #d1892a;
    --ink: #4a4748;
    --band: #0d0c0c;
    --band-text: #ffffff;
  }
  * { margin: 0; padding: 0; box-sizing: border-box; }
  html, body {
    width: 1200px; height: 736px; overflow: hidden;
    background: var(--bg);
    font-family: "Fira Sans Condensed", sans-serif;
  }
  .canvas {
    width: 1200px; height: 736px;
    display: flex; align-items: center; justify-content: center; gap: 60px;
  }
  .card {
    width: 480px; height: 274px; position: relative;
    box-shadow: 0 10px 30px rgba(0,0,0,0.12);
  }
  .card-front {
    background: var(--card-black);
    display: flex; align-items: center; justify-content: center;
  }
  .front-name {
    color: var(--gold); font-weight: 800; font-size: 50px; letter-spacing: 1px;
  }
  .card-back { background: var(--card-white); }
  .brand {
    position: absolute; left: 34px; top: 46px;
    color: var(--accent); font-size: 24px; font-weight: 500;
  }
  .person { position: absolute; left: 34px; top: 108px; }
  .person-name { color: var(--ink); font-size: 20px; font-weight: 400; }
  .person-role {
    color: var(--accent); font-size: 12px; font-weight: 500;
    letter-spacing: 0.8px; margin-top: 2px;
  }
  .divider {
    position: absolute; left: 222px; top: 50px; width: 1px; height: 110px;
    background: #d9c9ae;
  }
  .contacts {
    position: absolute; left: 240px; top: 58px; list-style: none;
  }
  .contacts li {
    display: flex; align-items: center; gap: 10px;
    color: var(--ink); font-size: 15px; height: 34px;
  }
  .contacts svg { width: 14px; height: 14px; flex: none; }
  .address-band {
    position: absolute; left: 0; right: 0; top: 218px; height: 28px;
    background: var(--band); color: var(--band-text);
    font-size: 15px; line-height: 28px; padding-left: 34px;
  }
</style>
</head>
<body>
<main class="canvas">
  <section class="card card-front">
    <h1 class="front-name">BRISK NO</h1>
  </section>

  <section class="card card-back">
    <div class="brand">Brisk NO</div>
    <div class="person">
      <div class="person-name">Lena Voskaric</div>
      <div class="person-role">DESIGNER</div>
    </div>
    <div class="divider"></div>
    <ul class="contacts">
      <li>
        <svg viewBox="0 0 14 14" fill="none" stroke="#d1892a" stroke-width="1.3"><rect x="3.5" y="1" width="7" height="12" rx="1.2"/><line x1="6" y1="11" x2="8" y2="11"/></svg>
        097 3208 415
      </li>
      <li>
        <svg viewBox="0 0 14 14" fill="none" stroke="#d1892a" stroke-width="1.3"><rect x="1" y="3" width="12" height="8.5"/><polyline points="1,3 7,8 13,3"/></svg>
        info@briskno.com.au
      </li>
      <li>
        <svg viewBox="0 0 14 14" fill="none" stroke="#d1892a" stroke-width="1.2"><circle cx="7" cy="7" r="5.8"/><ellipse cx="7" cy="7" rx="2.5" ry="5.8"/><line x1="1.2" y1="7" x2="12.8" y2="7"/></svg>
        www.briskno.com.au
      </li>
    </ul>
    <div class="address-band">Level 1, 214 Marlowe Avenue, Dunreath NO, 6120</div>
  </section>
</main>
</body>
</html>
```